Web Design Project - Quillmore Analytics

I am a Mechanical Engineer running a one person consulting firm at this point. The hope is to expand in the future, but for now I simply need a website that conveys a professional appearance, and allows potential and existing clients to find me. Website design displaying contact information, CV for download, capabilities, past projects, etc. I've included four examples below from companies that provided the same service. I've only provided these as general reference for the type of work I do and how others have chosen to display this information. The design is completely at your discretion.

I've included the current Logo in the uploaded files section. I will provide content as requried.

http://www.torvanmech.com/
http://www.halberic.com/
http://www.rumblaxsystems.com/
http://dorwickmotive.net/

Industry/Entity Type

Consulting

```html
<!DOCTYPE html>
<html lang="en">
<head>
<meta charset="utf-8">
<title>Quillmore Analytics</title>
<link rel="stylesheet" href="https://fonts.googleapis.com/css2?family=Michroma&family=Noto+Sans:wght@400;700&display=swap">
<style>
  :root {
    --page: #f7f7f7;
    --brand-blue: #0e9fde;
    --band-blue: #0a89c7;
    --accent-orange: #f2802a;
    --ink: #1c1c1c;
    --frame: #b4b4b4;
    --footer-grey: #75797b;
    --white: #ffffff;
    --social-light: #3fb6e8;
    --social-dark: #3b5998;
  }
  * { box-sizing: border-box; margin: 0; padding: 0; }
  html, body { width: 1200px; height: 1063px; overflow: hidden; }
  body {
    position: relative;
    background: var(--page);
    font-family: "Noto Sans", sans-serif;
    color: var(--ink);
  }
  .site-header {
    position: absolute; left: 168px; top: 0; width: 863px; height: 99px;
  }
  .brand-name {
    position: absolute; left: 4px; top: 48px;
    font-family: "Michroma", sans-serif;
    font-size: 19px; letter-spacing: 0.5px;
    color: var(--accent-orange);
    white-space: nowrap;
  }
  .social-links { position: absolute; right: 0; top: 45px; display: flex; gap: 6px; }
  .social-links a { display: block; width: 35px; height: 35px; border-radius: 3px; }
  .social-links .social-first { background: var(--social-light); }
  .social-links .social-second { background: var(--social-dark); }
  .main-nav {
    position: absolute; left: 168px; top: 99px; width: 863px; height: 42px;
    background: var(--brand-blue);
  }
  .main-nav a {
    position: absolute; top: 15px;
    font-family: "Michroma", sans-serif; font-size: 12px;
    font-variant: small-caps; letter-spacing: 1.5px;
    color: var(--white); text-decoration: none; white-space: nowrap;
  }
  .hero {
    position: absolute; left: 168px; top: 146px; width: 863px; height: 348px;
    background:
      radial-gradient(ellipse at 20% 40%, #8a6424 0%, transparent 45%),
      radial-gradient(ellipse at 85% 45%, #9c7229 0%, transparent 40%),
      radial-gradient(ellipse at 50% 60%, #5a4020 0%, transparent 35%),
      #120c06;
  }
  .hero-band {
    position: absolute; left: 168px; top: 497px; width: 863px; height: 16px;
    background: var(--band-blue);
  }
  .featured-title {
    position: absolute; left: 168px; top: 546px; width: 863px; text-align: center;
    font-family: "Michroma", sans-serif; font-size: 15px; font-weight: 400;
    font-variant: small-caps; letter-spacing: 2.5px; color: #111;
  }
  .featured-panel {
    position: absolute; left: 168px; top: 574px; width: 864px; height: 312px;
    border: 1px solid var(--frame); background: var(--page);
  }
  .project-card { position: absolute; top: 11px; width: 200px; }
  .project-photo { width: 200px; height: 152px; }
  .project-title {
    margin: 23px 0 0 6px;
    font-size: 16px; font-weight: 700; color: var(--accent-orange); line-height: 18px;
  }
  .project-text {
    margin-left: 6px; width: 186px;
    font-size: 12px; line-height: 14px; text-align: justify; color: var(--ink);
  }
  .photo-gears { background: linear-gradient(135deg, #d9d9d9, #7d7d7d 55%, #c6c6c6); }
  .photo-bolts { background: linear-gradient(135deg, #2b2030, #8c8594 50%, #3a3140); }
  .photo-assembly { background: linear-gradient(135deg, #bdbdbd, #5a5a5a 55%, #9a9a9a); }
  .photo-wheels { background: linear-gradient(135deg, #1f3c52, #9fc2d6 50%, #2c4d63); }
  .footer-band {
    position: absolute; left: 0; top: 943px; width: 1200px; height: 16px;
    background: var(--band-blue);
  }
  .site-footer {
    position: absolute; left: 0; top: 959px; width: 1200px; height: 104px;
    background: var(--footer-grey); color: var(--white);
    text-align: center; font-size: 14px; padding-top: 32px;
  }
</style>
</head>
<body>
  <header class="site-header">
    <div class="brand-name">Quillmore Analytics</div>
    <nav class="social-links" aria-label="Social links">
      <a class="social-first" href="#" aria-label="Social profile"></a>
      <a class="social-second" href="#" aria-label="Social profile"></a>
    </nav>
  </header>

  <nav class="main-nav">
    <a href="#" style="left:54px">Home</a>
    <a href="#" style="left:146px">About Quillmore</a>
    <a href="#" style="left:319px">Capabilities</a>
    <a href="#" style="left:477px">Past Projects</a>
    <a href="#" style="left:661px">CV</a>
    <a href="#" style="left:721px">Contact</a>
  </nav>

  <div class="hero" role="img" aria-label="Polished bronze pipework, valves and a large hand wheel"></div>
  <div class="hero-band"></div>

  <h2 class="featured-title">Featured Projects</h2>
  <section class="featured-panel">
    <article class="project-card" style="left:17px">
      <div class="project-photo photo-gears" role="img" aria-label="Interlocking steel gears"></div>
      <h3 class="project-title">Project 1</h3>
      <p class="project-text">Lorem ipsum dolor sit amet, consectetuer adipiscing elit, sed diam nonummy nibh euismod tincidunt ut laoreet dolore magna aliquam erat volutpat.</p>
    </article>
    <article class="project-card" style="left:227px">
      <div class="project-photo photo-bolts" role="img" aria-label="Rows of machined metal gear parts"></div>
      <h3 class="project-title">Project 2</h3>
      <p class="project-text">Lorem ipsum dolor sit amet, consectetuer adipiscing elit, sed diam nonummy nibh euismod tincidunt ut laoreet dolore.</p>
    </article>
    <article class="project-card" style="left:436px">
      <div class="project-photo photo-assembly" role="img" aria-label="Metal machine assembly"></div>
      <h3 class="project-title">Project 3</h3>
      <p class="project-text">Lorem ipsum dolor sit amet, consectetuer adipiscing elit, sed diam nonummy nibh euismod tincidunt ut laoreet dolore magna aliquam.</p>
    </article>
    <article class="project-card" style="left:646px">
      <div class="project-photo photo-wheels" role="img" aria-label="Blue-tinted gear wheels"></div>
      <h3 class="project-title">Project 4</h3>
      <p class="project-text">Lorem ipsum dolor sit amet, consectetuer adipiscing elit, sed diam nonummy nibh euismod tincidunt ut laoreet dolore.</p>
    </article>
  </section>

  <div class="footer-band"></div>
  <footer class="site-footer">© Quillmore Analytics 2013</footer>
</body>
</html>
```